11x 11 - KIVO Program Flyer

Introducing The KIVO PROGRAM

The BEST DPA Product on the Planet
* Lowest Zarn in the Industry - 580 Minimum
* Nothing Down - 100% GTU Purchase Financing
* One Submission, One Approval and One Closing
* No Income Limits, No DTI Restrictions, No Property Restrictions

Call (800) 471-9026 for more information

RLCB #738160
www.2ndlanehomes.com

```html
<!DOCTYPE html>
<html lang="en">
<head>
<meta charset="utf-8">
<title>KIVO Program Flyer</title>
<link href="https://fonts.googleapis.com/css2?family=Roboto:wght@400;700;900&family=Roboto+Condensed:wght@400;500;700&family=Roboto+Slab:wght@800&display=swap" rel="stylesheet">
<style>
  :root{
    --brand-blue:#0b5ca3;
    --brand-red:#d7271d;
    --stamp-red:#b3282d;
    --ink:#1d1d1b;
    --beige:#e6ddb6;
    --beige-light:#f4efd8;
    --page:#e9eaee;
    --white:#ffffff;
  }
  *{margin:0;padding:0;box-sizing:border-box;}
  html,body{width:720px;height:1200px;overflow:hidden;background:var(--page);}
  .flyer{
    position:absolute;left:20px;top:260px;width:680px;height:680px;
    background:var(--white);overflow:hidden;
    border-top:5px solid var(--brand-blue);
    box-shadow:0 2px 6px rgba(0,0,0,.15);
    font-family:"Roboto",sans-serif;
  }
  .backdrop{position:absolute;left:0;top:0;width:680px;height:680px;}
  .photo{
    position:absolute;left:0;top:0;width:680px;height:380px;
    background:
      linear-gradient(180deg,#ffffff 0%,#ffffff 28%,rgba(255,255,255,0) 45%,rgba(230,221,182,0) 82%,#e6ddb6 100%),
      linear-gradient(90deg,#e8ece6 0%,#d9c3a0 25%,#c9b79a 50%,#b9c4b4 75%,#e6e8e2 100%);
    clip-path:ellipse(345px 254px at 340px 219px);
  }
  .title{position:absolute;left:50px;top:44px;line-height:1;font-weight:900;}
  .title .the{display:block;color:var(--brand-blue);font-size:29px;}
  .title .name{display:block;color:var(--brand-red);font-size:94px;letter-spacing:-1px;margin-top:-2px;}
  .title .program{display:block;color:var(--brand-blue);font-size:49px;margin-top:-4px;}
  .brand{
    position:absolute;left:410px;top:70px;display:flex;align-items:center;gap:10px;
    color:var(--brand-blue);font-weight:700;font-size:21px;white-space:nowrap;
  }
  .brand .mark{width:34px;height:34px;border-radius:50%;background:var(--brand-blue);}
  .stamp{
    position:absolute;left:484px;top:323px;padding:3px 7px;white-space:nowrap;
    border:2px solid var(--stamp-red);color:var(--stamp-red);
    font-family:"Roboto Slab",serif;font-weight:800;font-size:15px;line-height:1.1;
    transform:rotate(-4deg);background:rgba(255,255,255,.3);
  }
  .headline{
    position:absolute;left:0;width:680px;top:368px;text-align:center;
    font-weight:700;font-size:27px;line-height:34px;color:var(--ink);white-space:nowrap;
    text-shadow:0 0 3px #fff,0 0 3px #fff,0 0 3px #fff;
  }
  .feature{
    position:absolute;top:421px;width:124px;height:124px;border-radius:50%;
    border:6px solid var(--brand-blue);
    background:radial-gradient(circle at 50% 35%,var(--beige-light),var(--beige) 70%);
    display:flex;flex-direction:column;align-items:center;justify-content:center;
    text-align:center;font-family:"Roboto Condensed",sans-serif;line-height:1.15;color:var(--ink);
    white-space:nowrap;
  }
  .feature .accent{color:var(--brand-blue);font-weight:500;}
  .feature .strong{font-weight:700;}
  .f1{left:56px}.f2{left:204px}.f3{left:351px}.f4{left:499px}
  .contact{
    position:absolute;left:27px;top:595px;width:625px;height:55px;border-radius:28px;
    background:var(--white);display:flex;align-items:center;white-space:nowrap;
    font-family:"Roboto Condensed",sans-serif;color:var(--brand-blue);font-weight:700;
  }
  .contact .cell{display:flex;align-items:center;gap:6px;height:38px;}
  .contact .phone{padding-left:14px;width:220px;}
  .contact .web{padding-left:12px;width:238px;border-left:2px solid var(--brand-blue);}
  .contact .license{padding-left:12px;border-left:2px solid var(--brand-blue);font-size:18px;}
  .phone .label{display:block;font-size:10px;font-weight:500;padding-left:2px;}
  .phone .number{display:block;font-size:25px;line-height:1;}
  .web .url{font-size:18px;}
</style>
</head>
<body>
<div class="flyer">
  <svg class="backdrop" viewBox="0 0 680 680" aria-hidden="true">
    <defs>
      <radialGradient id="arcFill" cx="50%" cy="70%" r="60%">
        <stop offset="0" stop-color="#efe8c9"/>
        <stop offset="1" stop-color="#e0d5a8"/>
      </radialGradient>
    </defs>
    <rect x="0" y="279" width="680" height="401" fill="var(--brand-blue)"/>
    <ellipse cx="340" cy="219" rx="345" ry="254" fill="url(#arcFill)"/>
    <path d="M110 385 H66 Q46 385 46 407 V462 Q46 484 62 484" fill="none" stroke="#1d1d1b" stroke-width="1.5"/>
    <path d="M570 385 H614 Q634 385 634 407 V462 Q634 484 618 484" fill="none" stroke="#1d1d1b" stroke-width="1.5"/>
    <path d="M176 484 H210 M324 484 H357 M471 484 H505" fill="none" stroke="#1d1d1b" stroke-width="1.5"/>
  </svg>

  <div class="photo" role="img" aria-label="Photo of a happy family carrying moving boxes into a bright new home"></div>

  <h1 class="title">
    <span class="the">THE</span>
    <span class="name">KIVO</span>
    <span class="program">PROGRAM</span>
  </h1>

  <div class="brand"><span class="mark"></span>2nd Lane Homes, Inc.</div>

  <div class="stamp">NO MONEY DOWN</div>

  <p class="headline">The BEST DPA Product on the Planet</p>

  <div class="feature f1">
    <span class="accent" style="font-size:12px">LOWEST ZARN IN<br>THE INDUSTRY</span>
    <span class="strong" style="font-size:18px;margin-top:3px">580 Minimum</span>
  </div>
  <div class="feature f2">
    <span class="accent strong" style="font-size:15px">NOTHING DOWN</span>
    <span class="strong" style="font-size:12px">100% GTU Purchase<br>Financing</span>
  </div>
  <div class="feature f3">
    <span class="accent" style="font-size:11px">ONE SUBMISSION,<br>ONE APPROVAL AND</span>
    <span class="strong" style="font-size:16px;margin-top:2px">ONE CLOSING</span>
  </div>
  <div class="feature f4">
    <span class="accent strong" style="font-size:14px">No Income Limits,</span>
    <span class="strong" style="font-size:12px">No DTI Restrictions,</span>
    <span class="strong" style="font-size:9.5px">No Property Restrictions</span>
  </div>

  <div class="contact">
    <div class="cell phone">
      <svg width="22" height="22" viewBox="0 0 24 24" aria-hidden="true">
        <circle cx="12" cy="12" r="12" fill="var(--brand-blue)"/>
        <path d="M8.2 6.5l2 2.3-1.1 1.6c.8 1.7 2 2.9 3.7 3.8l1.6-1.1 2.3 2-1.2 1.9c-4.4-.5-8-4.2-8.6-8.6z" fill="#fff"/>
      </svg>
      <div>
        <span class="label">for more information</span>
        <span class="number">(800) 471-9026</span>
      </div>
    </div>
    <div class="cell web">
      <svg width="24" height="24" viewBox="0 0 24 24" fill="none" stroke="var(--brand-blue)" stroke-width="1.6" aria-hidden="true">
        <circle cx="12" cy="12" r="10"/>
        <ellipse cx="12" cy="12" rx="4.5" ry="10"/>
        <path d="M2 12h20M4 7h16M4 17h16"/>
      </svg>
      <span class="url">www.2ndlanehomes.com</span>
    </div>
    <div class="cell license">RLCB #738160</div>
  </div>
</div>
</body>
</html>
```